International Clinical Software Company needs a new business card design

We are looking for a new business card design for our company that has recently expanded into the UK market, making us a multinational company.
After having rebranded our website and produced a new style guide, we are looking for a business card that is creative and attention grabbing, while being consistent with the style and colour scheme used on the new website, www.brookvale.example
We produce care management technology for the aged care market, but the main aspect we aim to communicate is the human element of our software, and the way it assists in providing better care for aged people, and stronger relationships between aged people and the staff that care for them.
Our current business card is a dark green with gold text, which makes the text quite difficult to read, not very aesthetically appealing and the colour scheme looks quite dated.
We would like something fresh and modern, that can still be colourful but doesn't use large blocks of dark colour, and uses the colours within our logo.
Something tying in with the leaves that are used in our logo could work quite nicely, along with the Autumn/Fall colours of soft greens, yellows and reds (also in our existing logo). However also happy to look at fresh, completely out of the box ideas we may not have yet considered.
Target Market(s)
The people that receive this business card work in the aged card or health industry and are either corporate/management level staff or clinical (Registered Nurses, care workers etc.)
Industry/Entity Type
Health Product
Contact Information for Business Card
Company Name - BrookvaleTech
Company locations: United Kingdom, Australia, New Zealand
Staff Details:
Staff name: Dermot Quill
Staff job title: Executive Chairman
Staff email: d.quill@brookvale.example
Office phone number: 01632 960418
Font styles to use
Other font styles liked:
- Calibri
Requirements
Must have
- Must include the BrookvaleTech brand name in it's current font
- Must include logo (3 leaves in gold circle)
- Must include Business Card Details
Nice to have
- Elements of gold
- White space
- Something autumn themed but not too cliched
Should not have
- No blue - used by a major competitor and we would like to differentiate from them
- Large blocks of dark green colour (the green that appears in our leaves on the logo on our current business card is the background colour and it is far too dark)

```html
<!DOCTYPE html>
<html lang="en">
<head>
<meta charset="utf-8">
<title>BrookvaleTech Business Card</title>
<link rel="stylesheet" href="https://fonts.googleapis.com/css2?family=Open+Sans:wght@300;400&display=swap">
<style>
  :root {
    --stage: #ece8de;
    --card: #ffffff;
    --card-shade: #eeeeec;
    --gold: #a79f77;
    --gold-deep: #8e865e;
    --band-start: #b3ab84;
    --band-end: #d9d4b8;
    --white-text: #ffffff;
    --leaf-yellow: #f2c24a;
    --leaf-orange: #e8893a;
    --leaf-light: #f7e3b0;
  }
  * { box-sizing: border-box; margin: 0; padding: 0; }
  html, body {
    width: 1200px; height: 780px; overflow: hidden;
    background: var(--stage);
    font-family: "Open Sans", Calibri, sans-serif;
  }
  .canvas {
    position: relative; width: 1200px; height: 780px;
    display: flex; align-items: center; justify-content: center; gap: 40px;
  }
  .card {
    position: relative; width: 540px; height: 310px;
    background: var(--card); overflow: hidden;
    box-shadow: 0 6px 18px rgba(80, 70, 40, .18);
  }

  /* Front */
  .card-front .band {
    position: absolute; left: 0; right: 0; top: 72px; height: 176px;
    background: linear-gradient(90deg, var(--band-start) 0%, var(--band-start) 55%, var(--band-end) 100%);
  }
  .card-front .brand {
    position: absolute; left: 26px; top: 22px;
    display: flex; align-items: center; gap: 16px;
  }
  .brand-circle {
    width: 104px; height: 104px; border-radius: 50%;
    background: var(--card); border: 3px solid var(--gold);
  }
  .card-front .brand-name {
    font-weight: 300; font-size: 40px; letter-spacing: .5px;
    color: var(--white-text); margin-top: 46px;
  }
  .person {
    position: absolute; left: 150px; top: 150px; color: var(--white-text);
  }
  .person-name { font-size: 21px; font-weight: 400; line-height: 1.1; }
  .person-title { font-size: 12px; font-weight: 300; margin-bottom: 12px; }
  .contact-line {
    display: flex; align-items: center; gap: 8px;
    font-size: 11px; font-weight: 300; line-height: 1.7;
  }
  .contact-line svg { width: 13px; height: 13px; flex: none; }
  .locations {
    position: absolute; left: 150px; top: 262px;
    font-size: 12px; font-weight: 400; color: var(--gold);
  }

  /* Back */
  .card-back {
    background: radial-gradient(ellipse at 70% 40%, #ffffff 0%, var(--card-shade) 100%);
  }
  .autumn-branch {
    position: absolute; left: 200px; top: 0; width: 340px; height: 230px;
    background:
      radial-gradient(ellipse at 55% 40%, var(--leaf-yellow) 0%, var(--leaf-orange) 45%, rgba(247, 227, 176, .6) 70%, rgba(255, 255, 255, 0) 85%);
  }
  .card-back .brand-name {
    position: absolute; left: 32px; bottom: 30px;
    font-weight: 300; font-size: 46px; letter-spacing: .5px;
    color: var(--gold);
  }
</style>
</head>
<body>
<main class="canvas">
  <section class="card card-front" aria-label="Business card front">
    <div class="band"></div>
    <div class="brand">
      <div class="brand-circle"></div>
      <span class="brand-name">BrookvaleTech</span>
    </div>
    <div class="person">
      <p class="person-name">Dermot Quill</p>
      <p class="person-title">Executive Chairman</p>
      <p class="contact-line">
        <svg viewBox="0 0 14 14" aria-hidden="true"><rect x="0.5" y="0.5" width="13" height="13" rx="2" fill="#ffffff"/><path d="M3 4.5h8v5H3z M3 4.5l4 3 4-3" fill="none" stroke="#a79f77" stroke-width="1"/></svg>
        d.quill@brookvale.example
      </p>
      <p class="contact-line">
        <svg viewBox="0 0 14 14" aria-hidden="true"><rect x="0.5" y="0.5" width="13" height="13" rx="2" fill="#ffffff"/><circle cx="7" cy="7" r="4" fill="none" stroke="#a79f77" stroke-width="1"/><path d="M3 7h8 M7 3c-2 2.5-2 5.5 0 8 M7 3c2 2.5 2 5.5 0 8" fill="none" stroke="#a79f77" stroke-width=".8"/></svg>
        www.brookvale.example
      </p>
    </div>
    <p class="locations">United Kingdom, Australia, New Zealand</p>
  </section>

  <section class="card card-back" aria-label="Business card back">
    <div class="autumn-branch" role="img" aria-label="Photograph of a branch with yellow and orange autumn leaves"></div>
    <span class="brand-name">BrookvaleTech</span>
  </section>
</main>
</body>
</html>
```